New singe page website for our software development company

We need a single webpage that includes information about our company, contact details and a job posting. It should scroll vertically with some cool animations and parallax scrolling effects.

We are a software development consulting company that writes custom software for our customers. The webpage should have graphics and illustrations that illustrate this.

Find our logo attached, it can be modified as needed.

Thanks for all the design. When looking through the various design it's clear to us, that car related images does not look right.

We got to have software design/engineering images instead.

Our unique selling points are:

• Custom software development
• Project Managment
• Industry Services
We want these displayed with some text and icons. The icons should either have the red/brown colour from our logo, or a colour that matches the design

Software

```html
<!DOCTYPE html>
<html lang="en">
<head>
<meta charset="utf-8">
<title>Keystone Consult — Software Development</title>
<link rel="stylesheet" href="https://fonts.googleapis.com/css2?family=Mulish:wght@300;400;700&family=Open+Sans:wght@400;600;700&display=swap">
<style>
:root{
  --brown:#4a0e05;
  --brown-dark:#2e0803;
  --cyan:#12a8c8;
  --paper:#f1f0ee;
  --band:#e6e6e6;
  --text-grey:#8d8d8d;
  --field:#a6a6a6;
  --ink:#222;
  --charcoal:#333;
}
*{box-sizing:border-box;margin:0;padding:0}
html,body{width:1200px;height:2571px;overflow:hidden}
body{position:relative;background:var(--paper);font-family:"Open Sans",sans-serif;color:var(--ink)}
.abs{position:absolute}

/* header */
.site-header{left:0;top:0;width:1200px;height:75px;background:linear-gradient(#fbfbfb,#dcdcdc);border-bottom:1px solid #c9c9c9}
.brand{left:103px;top:22px;display:flex;align-items:center;gap:8px;font-family:"Open Sans",sans-serif;font-weight:700;font-size:24px;color:var(--brown);white-space:nowrap}
.brand-mark{width:11px;height:11px;background:var(--brown)}
.main-nav{right:117px;top:29px;display:flex;gap:24px;font-size:15px;color:#111;white-space:nowrap}

/* hero */
.hero{left:0;top:75px;width:1200px;height:602px;background:radial-gradient(ellipse at 75% 30%,#5a3420 0%,#3a1a0e 40%,#1e0805 100%)}
.hero-title{left:165px;top:250px;width:830px;height:69px;background:rgba(0,0,0,.55);color:#fff;font-family:"Mulish",sans-serif;font-weight:300;font-size:41px;line-height:69px;text-align:center;white-space:nowrap}
.hero-title b{font-weight:700}
.hero-lead{left:190px;top:356px;width:780px;color:#fff;font-size:14px;line-height:19px;text-align:center}
.btn{height:45px;border-radius:23px;font-family:"Mulish",sans-serif;font-size:23px;line-height:45px;text-align:center;white-space:nowrap}
.btn-primary{left:391px;top:459px;width:192px;background:var(--cyan);color:#fff}
.btn-light{left:593px;top:459px;width:185px;background:linear-gradient(#fff,#e6e6e6);color:#222}
.hero-notch{left:560px;top:665px}

/* section headings */
.section-title{left:0;width:1200px;text-align:center;font-family:"Mulish",sans-serif;font-weight:400;font-size:48px;color:var(--brown);white-space:nowrap}
.section-title .dot{display:inline-block;width:7px;height:7px;border-radius:50%;background:var(--brown);vertical-align:middle;margin:0 22px}
.section-text{text-align:center;color:var(--text-grey);font-size:14.5px;line-height:22px}

/* about */
.about-icon{left:506px;top:738px;width:136px;height:136px;border-radius:50%;background:var(--brown);border:4px solid #fff;box-shadow:0 0 0 2px #d8d8d8}
.ribbon{height:26px;color:#fff;font-size:16px;font-weight:600;line-height:26px;text-align:center;white-space:nowrap;clip-path:polygon(0 0,100% 0,93% 50%,100% 100%,0 100%,7% 50%)}
.ribbon-brown{background:var(--brown)}
.ribbon-grey{background:#a3a3a3}

/* services */
.services{left:0;top:1265px;width:1200px;height:617px;background:var(--band)}
.service-icon{border-radius:50%;background:var(--brown);display:flex;align-items:center;justify-content:center}
.service-icon.featured{background:#fff;border:9px solid var(--brown)}
.service-name{font-family:"Open Sans",sans-serif;font-size:21px;color:#222;text-align:center;white-space:nowrap}
.service-text{font-size:12px;line-height:15px;text-align:center;color:#222}
.card-shade{top:1500px;width:10px;height:190px;background:linear-gradient(90deg,rgba(0,0,0,0),rgba(0,0,0,.05))}

/* contact */
.contact-icon{width:74px;height:74px;border-radius:50%;background:var(--charcoal);display:flex;align-items:center;justify-content:center}
.contact-label{font-size:16px;color:var(--brown);white-space:nowrap}
.field{background:var(--field);color:#fff;font-size:13.5px;padding-left:14px;line-height:38px;white-space:nowrap}
.btn-send{left:449px;top:2424px;width:136px;height:39px;border-radius:20px;background:var(--brown);color:#fff;font-size:18px;font-weight:600;line-height:39px;text-align:center;letter-spacing:1px}

/* footer */
.footer-rule{left:120px;top:2515px;width:960px;height:1px;background:#d6d6d6}
.copyright{left:0;top:2535px;width:1200px;text-align:center;font-size:13px;color:#222}
</style>
</head>
<body>

<header class="site-header abs">
  <div class="brand abs"><span class="brand-mark"></span>Keystone Consult</div>
  <nav class="main-nav abs"><span>Sign In</span><span>Log In</span><span>How it works</span></nav>
</header>

<section class="hero abs" role="img" aria-label="Blurred photograph of a developer workspace with monitors and desk"></section>
<h1 class="hero-title abs">Keystone Consult <b>Software Development</b></h1>
<p class="hero-lead abs">Lorem Ipsum is simply dummy text of the printing and typesetting industry. Lorem Ipsum has been the industry's standard dummy text ever since the 1500s, when an unknown printer took a galley of type and scrambled it to make a type specimen book. It has survived not only five centuries, but also the leap into electronic typesetting.</p>
<div class="btn btn-primary abs">Read More</div>
<div class="btn btn-light abs">Contact Us</div>
<svg class="hero-notch abs" width="80" height="24" viewBox="0 0 80 24">
  <path d="M0 12 H22 L30 4 L40 12 L50 4 L58 12 H80" fill="none" stroke="#8a1a0a" stroke-width="3"/>
  <polygon points="32,12 40,4 48,12 40,20" fill="#8a1a0a"/>
</svg>

<!-- about -->
<div class="about-icon abs">
  <svg width="128" height="128" viewBox="0 0 128 128">
    <g fill="#fff">
      <circle cx="44" cy="50" r="10"/><path d="M26 82 q0-20 18-20 q18 0 18 20z"/>
      <circle cx="84" cy="50" r="10"/><path d="M66 82 q0-20 18-20 q18 0 18 20z"/>
      <circle cx="64" cy="44" r="13"/><path d="M40 88 q0-26 24-26 q24 0 24 26z"/>
    </g>
  </svg>
</div>
<h2 class="section-title abs" style="top:886px"><span class="dot"></span>About Us<span class="dot"></span></h2>
<p class="section-text abs" style="left:214px;top:973px;width:772px">It is a long established fact that a reader will be distracted by the readable content of a page when looking at its layout. The point of using Lorem Ipsum is that it has a more-or-less normal distribution of letters, as opposed to using 'Content here, content here', making it look like readable English. Many desktop publishing packages and web page editors now use Lorem Ipsum as their default model text, and a search for 'lorem ipsum' will uncover many web sites still in their infancy. Various versions have evolved over the years, sometimes by accident, some-times on purpose (injected humour and the like).</p>
<div class="ribbon ribbon-brown abs" style="left:463px;top:1157px;width:238px">READ MORE</div>

<!-- services -->
<section class="services abs"></section>
<h2 class="section-title abs" style="top:1320px"><span class="dot"></span>Our Service<span class="dot"></span></h2>
<p class="section-text abs" style="left:214px;top:1409px;width:772px;font-size:14px">It is a long established fact that a reader will be distracted by the readable content of a page when looking at its layout. The point of using Lorem Ipsum is that it has a more-or-less normal distribution of letters, as opposed to using 'Content here, content here', making it look like readable English.</p>

<div class="card-shade abs" style="left:402px"></div>
<div class="card-shade abs" style="left:762px;transform:scaleX(-1)"></div>

<div class="service-icon abs" style="left:159px;top:1522px;width:144px;height:144px">
  <svg width="80" height="80" viewBox="0 0 80 80" fill="none" stroke="#fff" stroke-width="3">
    <rect x="10" y="16" width="60" height="40" rx="3"/><path d="M32 56 v10 M48 56 v10 M26 66 h28"/>
    <rect x="26" y="8" width="16" height="26" rx="2" fill="#4a0e05"/><rect x="44" y="22" width="12" height="20" rx="2" fill="#4a0e05"/>
  </svg>
</div>
<div class="service-name abs" style="left:81px;top:1680px;width:300px">Software Development</div>
<p class="service-text abs" style="left:111px;top:1722px;width:240px">Lorem Ipsum is simply dummy text of the printing and typesetting industry. Lorem</p>
<div class="ribbon ribbon-grey abs" style="left:137px;top:1773px;width:199px">READ MORE</div>

<div class="service-icon featured abs" style="left:500px;top:1508px;width:172px;height:172px">
  <svg width="96" height="96" viewBox="0 0 96 96" fill="none" stroke="#4a0e05" stroke-width="4">
    <rect x="10" y="26" width="76" height="54" rx="4"/><path d="M36 26 v-8 h24 v8"/>
    <path d="M24 30 v46 M72 30 v46"/><path d="M46 46 v12 l4-3 3 6" stroke-width="2.5"/>
  </svg>
</div>
<div class="service-name abs" style="left:436px;top:1697px;width:300px;font-size:30px">Post a Job</div>
<p class="service-text abs" style="left:466px;top:1754px;width:240px">Lorem Ipsum is simply dummy text of the printing and typesetting industry. Lorem</p>
<div class="ribbon ribbon-grey abs" style="left:489px;top:1809px;width:212px">READ MORE</div>

<div class="service-icon abs" style="left:862px;top:1522px;width:144px;height:144px">
  <svg width="84" height="84" viewBox="0 0 84 84" fill="none" stroke="#fff" stroke-width="3">
    <rect x="16" y="22" width="52" height="34" rx="3"/><path d="M8 62 h68 l-4 6 h-60z"/>
    <path d="M34 32 l-8 7 8 7 M50 32 l8 7 -8 7 M45 30 l-6 18"/><path d="M64 8 v8 M60 12 h8 M56 16 v4 M54 18 h4" stroke-width="2"/>
  </svg>
</div>
<div class="service-name abs" style="left:784px;top:1680px;width:300px">Independent Development</div>
<p class="service-text abs" style="left:814px;top:1722px;width:240px">Lorem Ipsum is simply dummy text of the printing and typesetting industry. Lorem</p>
<div class="ribbon ribbon-grey abs" style="left:847px;top:1773px;width:200px">READ MORE</div>

<!-- contact -->
<h2 class="section-title abs" style="top:1988px"><span class="dot"></span>Contact Us<span class="dot"></span></h2>
<p class="section-text abs" style="left:250px;top:2068px;width:710px;font-size:15.5px;line-height:25px">It is a long established fact that a reader will be distracted by the readable content of a page when looking at its layout. The point of using Lorem Ipsum is that it has a more-or-less</p>

<div class="contact-icon abs" style="left:143px;top:2166px">
  <svg width="40" height="40" viewBox="0 0 40 40" fill="none" stroke="#fff" stroke-width="2.2"><rect x="4" y="9" width="32" height="22" rx="2"/><path d="M4 10 l16 12 16-12 M4 30 l12-10 M36 30 l-12-10"/></svg>
</div>
<div class="contact-label abs" style="left:237px;top:2188px">hi@keystoneconsult.com</div>

<div class="contact-icon abs" style="left:143px;top:2243px">
  <svg width="40" height="40" viewBox="0 0 40 40"><path fill="#fff" d="M11 5 l6 8 -3 4 q3 7 9 10 l4-3 8 6 -4 6 q-12 0-21-10 Q5 23 6 10z"/></svg>
</div>
<div class="contact-label abs" style="left:231px;top:2268px">808 555 0142</div>

<div class="contact-icon abs" style="left:143px;top:2323px">
  <svg width="40" height="40" viewBox="0 0 40 40"><circle cx="20" cy="20" r="13" fill="none" stroke="#fff" stroke-width="3"/></svg>
</div>
<div class="contact-label abs" style="left:237px;top:2349px">keystoneconsult</div>

<div class="field abs" style="left:447px;top:2173px;width:326px;height:38px">Name (required)</div>
<div class="field abs" style="left:782px;top:2173px;width:284px;height:38px">Last Name</div>
<div class="field abs" style="left:447px;top:2227px;width:326px;height:38px">Phone Number</div>
<div class="field abs" style="left:782px;top:2227px;width:284px;height:38px">Email (required)</div>
<div class="field abs" style="left:447px;top:2280px;width:619px;height:128px;line-height:30px">Your Message</div>
<div class="btn-send abs">SEND</div>

<div class="footer-rule abs"></div>
<p class="copyright abs">Copyright 2014 keystoneconsult. All Rights Reserved.</p>

</body>
</html>
```